Marwick Estate Services (Handyman / Home Improvement Company)

Looking for a double sided professional looking business card with Logo attached to be highlighted on one side and throwing in an image of a handyman as an option would be nice to see as well. We are a company focused on providing quality Handyman and Home improvement services in a timely manner that is done right the first time with integrity

Industry/Entity Type

Handyman / Home Improvement

Contact Information for Business Card

(LOGO, Name, Mobile and office phone numbers, email) on front side of card, (the words "The SOLUTION to all of your Handyman and Home Improvement needs" followed by "Family Owned and Operated" at the very bottom) on the back.

Colors
EB3D1F
EC4F4E
F09395
F8D3D4
FCEDEE

Requirements
Must have
• Red, Gray, Black Color scheme
Should not have
• No Yellow or Blue colors

```html
<!DOCTYPE html>
<html lang="en">
<head>
<meta charset="utf-8">
<title>Marwick Estate Services – Business Card</title>
<link rel="stylesheet" href="https://fonts.googleapis.com/css2?family=Michroma&family=Poppins:wght@400;600&display=swap">
<style>
  :root {
    --page: #e7e8ea;
    --card: #050607;
    --red: #eb3d1f;
    --red-soft: #ec4f4e;
    --pink: #f09395;
    --blush: #f8d3d4;
    --white: #ffffff;
    --rule: #9a9a9a;
  }
  * { box-sizing: border-box; margin: 0; padding: 0; }
  html, body { width: 1194px; height: 1200px; overflow: hidden; background: var(--page); }
  body { position: relative; font-family: "Poppins", sans-serif; }

  .card {
    position: absolute; left: 307px; width: 579px; height: 331px;
    background: var(--card); overflow: hidden;
  }
  .card--front { top: 166px; }
  .card--back { top: 638px; }

  .brand {
    position: absolute; display: flex; align-items: center; gap: 8px;
    font-family: "Michroma", sans-serif; color: var(--red);
    font-size: 12px; line-height: 1.35; letter-spacing: 1px;
  }
  .brand__dot { width: 14px; height: 14px; border-radius: 50%; background: var(--red); flex: none; }
  .card--front .brand { left: 30px; top: 52px; width: 160px; }
  .card--back .brand { left: 200px; top: 92px; width: 200px; font-size: 15px; }
  .card--back .brand__dot { width: 18px; height: 18px; }

  .holder { position: absolute; left: 31px; top: 164px; }
  .holder__name {
    font-family: "Michroma", sans-serif; font-weight: 400; color: var(--red);
    font-size: 17px; letter-spacing: 3px; -webkit-text-stroke: 0.6px var(--red);
  }
  .holder__role {
    margin-top: 4px; color: var(--white); font-size: 13px; letter-spacing: 2.2px;
  }
  .holder__rule { position: absolute; left: 95px; top: 203px; width: 281px; height: 1px; background: var(--rule); }

  .contacts { position: absolute; left: 31px; top: 220px; list-style: none; }
  .contacts li {
    display: flex; align-items: center; gap: 16px; height: 29px;
    color: var(--white); font-size: 12.5px; letter-spacing: 0.8px;
  }
  .contacts svg { width: 17px; height: 17px; flex: none; }

  .mascot {
    position: absolute; left: 377px; top: 12px; width: 180px; height: 300px;
    border-radius: 90px 90px 10px 10px;
    background: linear-gradient(180deg, #c93a33 0%, #e9a98a 30%, #2a2a2a 55%, #2f4f8c 100%);
  }
  .card--back .mascot { top: 11px; opacity: 0.3; }

  .tagline {
    position: absolute; left: 0; width: 100%; top: 212px; text-align: center;
    font-family: "Michroma", sans-serif; color: var(--white);
    font-size: 12.5px; line-height: 26px; letter-spacing: 2.6px;
    -webkit-text-stroke: 0.3px var(--white);
  }
  .motto {
    position: absolute; left: 0; width: 100%; top: 276px; text-align: center;
    color: var(--red); font-weight: 600; font-size: 12px; letter-spacing: 3px;
  }

  .band { position: absolute; left: 0; bottom: 0; width: 579px; height: 19px; }
</style>
</head>
<body>

<section class="card card--front">
  <div class="brand"><span class="brand__dot"></span><span>MARWICK ESTATE SERVICES</span></div>

  <div class="holder">
    <h1 class="holder__name">DANIEL HARTLEY</h1>
    <p class="holder__role">OWNER</p>
  </div>
  <div class="holder__rule"></div>

  <ul class="contacts">
    <li>
      <svg viewBox="0 0 20 20"><circle cx="10" cy="10" r="8.5" fill="none" stroke="#eb3d1f" stroke-width="1.3"/><path d="M7 6.2l1.5-.4 1 2.2-1 .8c.5 1.2 1.3 2 2.5 2.5l.8-1 2.2 1-.4 1.5c-3.6.3-7-3.1-6.6-6.6z" fill="none" stroke="#eb3d1f" stroke-width="1"/></svg>
      <span>(555) 304-8127</span>
    </li>
    <li>
      <svg viewBox="0 0 20 20"><circle cx="10" cy="10" r="8.5" fill="none" stroke="#eb3d1f" stroke-width="1.3"/><rect x="7" y="5" width="6" height="10" rx="1" fill="none" stroke="#eb3d1f" stroke-width="1.1"/></svg>
      <span>(555) 304-8127</span>
    </li>
    <li>
      <svg viewBox="0 0 20 20"><circle cx="10" cy="10" r="8.5" fill="none" stroke="#eb3d1f" stroke-width="1.3"/><rect x="5.5" y="7" width="9" height="6.5" fill="none" stroke="#eb3d1f" stroke-width="1.1"/><path d="M5.5 7l4.5 3.5L14.5 7" fill="none" stroke="#eb3d1f" stroke-width="1.1"/></svg>
      <span>danielhartley@mail.com</span>
    </li>
  </ul>

  <div class="mascot" role="img" aria-label="Illustration of a smiling handyman in a red cap holding a hammer, arms crossed"></div>

  <svg class="band" viewBox="0 0 579 19" preserveAspectRatio="none" aria-hidden="true">
    <defs>
      <linearGradient id="bandFront" x1="0" x2="1">
        <stop offset="0" stop-color="#fcedee"/>
        <stop offset="0.55" stop-color="#f09395"/>
        <stop offset="1" stop-color="#eb3d1f"/>
      </linearGradient>
    </defs>
    <rect width="579" height="19" fill="url(#bandFront)"/>
    <rect y="0" width="320" height="6" fill="url(#bandFront)" opacity="0.6"/>
    <polygon points="0,8 322,8 330,0 336,0 324,12 0,12" fill="#050607"/>
    <polygon points="0,12 324,12 322,14 0,14" fill="#ffffff" opacity="0.6"/>
  </svg>
</section>

<section class="card card--back">
  <div class="mascot" role="img" aria-label="Faint illustration of the handyman mascot"></div>

  <div class="brand"><span class="brand__dot"></span><span>MARWICK ESTATE SERVICES</span></div>

  <p class="tagline">YOUR SOLUTION TO ALL OF YOUR HANDYMAN<br>AND HOME IMPROVEMENT NEEDS</p>
  <p class="motto">Family Owned and Operated</p>

  <svg class="band" viewBox="0 0 579 19" preserveAspectRatio="none" aria-hidden="true">
    <defs>
      <linearGradient id="bandBack" x1="0" x2="1">
        <stop offset="0" stop-color="#fcedee"/>
        <stop offset="0.55" stop-color="#f09395"/>
        <stop offset="1" stop-color="#eb3d1f"/>
      </linearGradient>
    </defs>
    <rect width="579" height="19" fill="url(#bandBack)"/>
    <polygon points="0,8 322,8 330,0 336,0 324,12 0,12" fill="#050607"/>
    <polygon points="0,12 324,12 322,14 0,14" fill="#ffffff" opacity="0.6"/>
  </svg>
</section>

</body>
</html>
```